Website page design

Hi, I need to improve the look of my homepage and the final offer page of my website. www.Pebble7dock.com We have an orvex buyback program where we purchase used orvex products from consumers nationwide. If you would go click through a sample offer on the site, you will the last view final offer page where we give you a cash offer for you site. I would like to keep the red and white colors since my logo is red and white. Please pay attention to the information shown on the homepage now, it is important for me to show the visitors this information on the home page. I would also love to give the users a friendly and inviting look when clicking on the options of orvex products on the home page.

Target Market(s)

Orvex electronics consumers

Number of Pages Required

2 page

Requirements
Nice to have
• On the final offer page, i would love for the offer to give an exciting look for the pebble 7 dock offer, and a boring look for the orvex buy back offer. At the final offer page you will my websites offer ( Your Pebble7dock Offer ) vs ( Orvex buyback program offer ) which is my competitor.

```html
<!DOCTYPE html>
<html lang="en">
<head>
<meta charset="utf-8">
<title>Pebble7dock – Home</title>
<link href="https://fonts.googleapis.com/css2?family=Saira+Semi+Condensed:wght@500;600;700&family=Open+Sans:wght@400;600&family=Poppins:wght@400;500&display=swap" rel="stylesheet">
<style>
:root{
  --red:#c8102e;
  --red-dark:#a50d25;
  --ink:#1d1d22;
  --text:#333;
  --muted:#666;
  --grey-bg:#ebebeb;
  --footer:#20222f;
  --line:#dadada;
  --white:#fff;
}
*{box-sizing:border-box;margin:0;padding:0}
html,body{width:1200px;height:3231px;overflow:hidden}
body{position:relative;background:var(--white);font-family:"Open Sans",sans-serif;color:var(--text)}
.abs{position:absolute}
.head{font-family:"Saira Semi Condensed",sans-serif}

/* header */
.site-header{left:0;top:0;width:1200px;height:93px;background:var(--white);box-shadow:0 2px 4px rgba(0,0,0,.15);z-index:2}
.brand{left:144px;top:10px;display:flex;align-items:center;gap:16px;height:72px}
.brand-mark{width:72px;height:72px;border:2px solid var(--line);display:flex;align-items:center;justify-content:center}
.brand-mark span{width:50px;height:42px;background:var(--red)}
.brand-name{font-family:"Saira Semi Condensed",sans-serif;font-weight:600;font-size:32px;color:var(--ink)}
.nav{top:34px;font-family:"Saira Semi Condensed",sans-serif;font-size:18px;font-weight:500;color:var(--ink);letter-spacing:.5px}
.login{left:953px;top:29px;width:105px;height:33px;background:var(--red);color:var(--white);font-family:"Saira Semi Condensed",sans-serif;font-weight:700;font-size:16px;display:flex;align-items:center;justify-content:center;gap:6px}

/* hero */
.hero{left:0;top:93px;width:1200px;height:597px;background:linear-gradient(100deg,#8c8b89 0%,#b5b3b0 40%,#9a9997 70%,#7c7b79 100%)}
.hero-title{left:143px;top:208px;font-family:"Saira Semi Condensed",sans-serif;font-weight:700;font-size:52px;color:#222;letter-spacing:1px}
.hero-text{left:143px;top:278px;width:320px;font-size:15px;line-height:29px;color:#222}
.btn-red{background:var(--red);color:var(--white);font-family:"Saira Semi Condensed",sans-serif;font-weight:700;display:flex;align-items:center;justify-content:center}
.hero-btn{left:145px;top:387px;width:135px;height:44px;font-size:16px;box-shadow:0 2px 4px rgba(0,0,0,.3)}
.arrow-circle{width:32px;height:32px;border-radius:50%;background:#3a3a3a;border:2px solid #ddd}

/* badges */
.badges{left:0;top:690px;width:1200px;height:128px;border:1px solid var(--line);background:var(--white)}
.badge{background:#e4e4e4;border-radius:4px}

/* section titles */
.section-title{width:1200px;left:0;text-align:center;font-family:"Saira Semi Condensed",sans-serif;font-weight:600;color:var(--ink)}

/* devices */
.device{top:962px;width:298px;height:364px}
.device .label{position:absolute;left:0;bottom:0;width:100%;height:57px;background:rgba(25,25,30,.85);color:var(--white);font-family:"Saira Semi Condensed",sans-serif;font-weight:600;font-size:19px;display:flex;align-items:center;justify-content:center;letter-spacing:.5px}
.device-active{left:301px;top:1269px;width:298px;height:128px;background:var(--red);color:var(--white);padding:12px 18px}
.device-active h3{font-family:"Saira Semi Condensed",sans-serif;font-size:19px;font-weight:600}
.device-active p{font-size:14px;line-height:22px;margin-top:6px}
.device-active .more{font-family:"Saira Semi Condensed",sans-serif;font-weight:700;font-size:13px;margin-top:6px;display:flex;align-items:center;gap:6px}

/* steps */
.step-title{font-family:"Saira Semi Condensed",sans-serif;font-weight:600;font-size:19px;color:var(--ink);text-align:center;width:300px}
.step-text{font-size:13.5px;line-height:25.5px;color:#444;text-align:center;width:270px}

/* testimonials */
.reviews{left:0;top:2020px;width:1200px;height:427px;background:linear-gradient(115deg,#d01227 0%,#c4101f 45%,#a80d1c 100%)}
.reviews-title{left:0;top:2090px;width:1200px;text-align:center;color:var(--white);font-family:"Saira Semi Condensed",sans-serif;font-weight:700;font-size:42px}
.reviews-title em{font-weight:500}
.avatar{width:68px;height:68px;border-radius:50%;border:3px solid var(--white);background:#c9b8ad}
.quote{width:205px;color:var(--white);font-family:"Poppins",sans-serif;font-size:12.5px;line-height:22.5px}
.quote b{font-family:"Saira Semi Condensed",sans-serif;font-size:16px;margin-right:6px}
.reviewer{color:var(--white);font-family:"Poppins",sans-serif;font-style:italic;font-size:14px}

/* newsletter */
.newsletter{left:0;top:2447px;width:1200px;height:400px;background:var(--grey-bg)}
.news-title{left:0;top:2514px;width:1200px;text-align:center;font-family:"Saira Semi Condensed",sans-serif;font-weight:700;font-size:34px;color:var(--ink)}
.news-title span{color:var(--red)}
.news-text{left:300px;top:2575px;width:600px;text-align:center;font-size:14px;line-height:26px;color:#444}
.email{left:329px;top:2662px;width:391px;height:39px;border-radius:20px;background:var(--white);font-family:"Poppins",sans-serif;font-size:12px;color:#666;padding:12px 18px}
.subscribe{left:736px;top:2661px;width:136px;height:40px;border-radius:20px;font-size:16px}

/* footer */
.footer-col-title{font-family:"Saira Semi Condensed",sans-serif;font-weight:600;font-size:19px;color:var(--white)}
.footer-text{font-family:"Poppins",sans-serif;font-size:14px;color:var(--white);line-height:32px}
.foot-brand-mark{left:187px;top:2870px;width:91px;height:81px;background:var(--white);display:flex;align-items:center;justify-content:center}
.foot-brand-mark span{width:64px;height:50px;background:var(--red)}
.foot-brand-name{left:130px;top:2968px;width:205px;text-align:center;font-family:"Saira Semi Condensed",sans-serif;font-weight:600;font-size:32px;color:var(--white)}
.social{width:32px;height:32px;border-radius:50%;border:2px solid var(--white)}
.copyright{left:0;top:3169px;width:1200px;text-align:center;font-family:"Poppins",sans-serif;font-size:14px;color:var(--white)}
</style>
</head>
<body>

<header class="abs site-header">
  <div class="abs brand"><div class="brand-mark"><span></span></div><div class="brand-name">Pebble7dock</div></div>
  <div class="abs nav" style="left:729px">SELL</div>
  <div class="abs nav" style="left:798px">TRACK</div>
  <div class="abs nav" style="left:881px">JOIN</div>
  <div class="abs login"><svg width="11" height="13" viewBox="0 0 11 13"><rect x="0" y="5" width="11" height="8" fill="#fff"/><path d="M2.5 5V3.5a3 3 0 0 1 6 0V5" stroke="#fff" stroke-width="1.8" fill="none"/></svg>LOGIN</div>
</header>

<section class="abs hero" role="img" aria-label="Photo of an open laptop beside its white retail box and charger on a grey reflective desk"></section>
<h1 class="abs hero-title">PEBBLE7DOCK</h1>
<p class="abs hero-text">Sed ut perspiciatis unde omnis iste natus voluptatem accusantium doloremque laudantium, totam rem aperiam</p>
<div class="abs btn-red hero-btn">READ MORE</div>
<svg class="abs" style="left:67px;top:364px" width="34" height="34" viewBox="0 0 34 34"><circle cx="17" cy="17" r="15" fill="#333" stroke="#ddd" stroke-width="2"/><path d="M19 11l-6 6 6 6" stroke="#fff" stroke-width="2" fill="none"/></svg>
<svg class="abs" style="left:1099px;top:366px" width="34" height="34" viewBox="0 0 34 34"><circle cx="17" cy="17" r="15" fill="#333" stroke="#ddd" stroke-width="2"/><path d="M15 11l6 6-6 6" stroke="#fff" stroke-width="2" fill="none"/></svg>

<section class="abs badges">
  <div class="abs badge" style="left:245px;top:42px;width:116px;height:44px"></div>
  <div class="abs badge" style="left:435px;top:44px;width:245px;height:40px"></div>
  <div class="abs badge" style="left:748px;top:40px;width:62px;height:48px"></div>
  <div class="abs badge" style="left:865px;top:36px;width:82px;height:56px"></div>
</section>

<h2 class="abs section-title" style="top:862px;font-size:38px">Select Your Device to Receive an Instant Quote</h2>

<div class="abs device" style="left:0;background:linear-gradient(135deg,#d7a36c,#e6c39a 50%,#6a8fbf)" role="img" aria-label="Photo of a hand holding a smartphone"><div class="label">ORVEX PHONE</div></div>
<div class="abs device" style="left:301px;background:linear-gradient(160deg,#f2f2f2,#e2e2e2);height:307px" role="img" aria-label="Photo of two tablets with colourful screens"></div>
<div class="abs device-active">
  <h3>ORVEX TAB</h3>
  <p>Sed ut perspiciatis unde omnis iste natus sit voluptatem accusant</p>
  <div class="more">READ MORE <svg width="11" height="11" viewBox="0 0 11 11"><circle cx="5.5" cy="5.5" r="4.5" stroke="#fff" stroke-width="1.4" fill="none"/><path d="M4.5 3.5l2 2-2 2" stroke="#fff" stroke-width="1.3" fill="none"/></svg></div>
</div>
<div class="abs device" style="left:602px;background:linear-gradient(150deg,#6f6f70,#2f2f31 60%,#4a4a4c)" role="img" aria-label="Photo of a laptop keyboard and box"><div class="label">ORVEX BOOK</div></div>
<div class="abs device" style="left:903px;width:297px;background:linear-gradient(150deg,#7a5a8c,#c98a55 45%,#4a3a2e)" role="img" aria-label="Photo of a desktop computer on a wooden desk"><div class="label">ORVEX DESK</div></div>
<svg class="abs" style="left:256px;top:1360px" width="24" height="20" viewBox="0 0 24 20"><path d="M22 10H3M11 2l-8 8 8 8" stroke="#555" stroke-width="3" fill="none"/></svg>
<svg class="abs" style="left:616px;top:1360px" width="24" height="20" viewBox="0 0 24 20"><path d="M2 10h19M13 2l8 8-8 8" stroke="#555" stroke-width="3" fill="none"/></svg>

<h2 class="abs section-title" style="top:1472px;font-size:40px">How It Works</h2>

<div class="abs" style="left:40px;top:1800px;width:1120px;height:220px;background:linear-gradient(180deg,rgba(255,255,255,0),rgba(225,225,225,.55))" role="img" aria-label="Faint line drawing of a city skyline"></div>

<svg class="abs" style="left:0;top:1550px" width="1200" height="220" viewBox="0 0 1200 220">
  <path d="M335 145 C370 180 410 185 438 183 C480 178 510 140 530 110" stroke="#999" stroke-width="1.3" stroke-dasharray="2 3" fill="none"/>
  <path d="M665 70 C700 20 760 10 763 25 C800 40 830 80 868 120" stroke="#999" stroke-width="1.3" stroke-dasharray="2 3" fill="none"/>
  <circle cx="438" cy="183" r="8" fill="#444"/><circle cx="763" cy="25" r="8" fill="#444"/>
  <circle cx="270" cy="144" r="66" fill="#fff" stroke="#ddd" stroke-width="5"/>
  <circle cx="270" cy="144" r="55" fill="#fff" stroke="#ccc" stroke-width="2"/>
  <g stroke="#c8102e" stroke-width="2" fill="none"><rect x="248" y="114" width="32" height="58" rx="3"/><path d="M255 124h4v4h-4zM264 124h4v4h-4zM273 124h4v4h-4zM255 134h4v4h-4zM264 134h4v4h-4zM255 144h4v4h-4zM264 144h4v4h-4zM255 154h4v4h-4z"/><path d="M276 150c6 2 12 10 14 22"/></g>
  <circle cx="598" cy="88" r="80" fill="#fff" stroke="#ddd" stroke-width="5"/>
  <circle cx="598" cy="88" r="66" fill="#fff" stroke="#ccc" stroke-width="2"/>
  <circle cx="598" cy="88" r="57" fill="#c8102e"/>
  <g stroke="#fff" stroke-width="2.5" fill="none"><rect x="566" y="68" width="40" height="30"/><path d="M606 76h14l8 10v12h-22"/><circle cx="578" cy="102" r="5"/><circle cx="616" cy="102" r="5"/><path d="M577 82l6 6 11-11"/></g>
  <circle cx="928" cy="144" r="66" fill="#fff" stroke="#ddd" stroke-width="5"/>
  <circle cx="928" cy="144" r="55" fill="#fff" stroke="#ccc" stroke-width="2"/>
  <g stroke="#c8102e" stroke-width="2" fill="none"><path d="M904 158l12-6 14 4 12-8M952 130l-12 4-14-4-12 8"/><rect x="898" y="150" width="8" height="16"/><rect x="950" y="122" width="8" height="16"/><circle cx="928" cy="142" r="6"/></g>
</svg>
<div class="abs step-title" style="left:120px;top:1786px">GET AN OFFER</div>
<p class="abs step-text" style="left:135px;top:1823px">Less than a minute ut perspiciatis unde omnis iste natus error sit voluptatem accusantium doloremque laudantium, totam rem aperiam, eaque</p>
<div class="abs step-title" style="left:448px;top:1740px">SHIP IT FREE</div>
<p class="abs step-text" style="left:463px;top:1777px">We provide a pre-paid shipping label ut perspiciatis unde omnis iste natus error sit voluptatem accusantium doloremque laudantium, totam rem aperiam</p>
<div class="abs step-title" style="left:778px;top:1786px">GET PAID FAST</div>
<p class="abs step-text" style="left:793px;top:1823px">QuickWallet, check or bank transfer ut perspiciatis unde omnis iste natus error sit voluptatem accusantium doloremque laudantium, totam rem</p>

<section class="abs reviews" role="img" aria-label="Red-tinted photo of a hand holding a smartphone"></section>
<h2 class="abs reviews-title">WHAT <em>OUR CLIENTS SAY</em></h2>

<div class="abs avatar" style="left:148px;top:2204px" role="img" aria-label="Client portrait"></div>
<p class="abs quote" style="left:234px;top:2204px"><b>//</b>At vero eos et accusamus et iustodio dignissimos ducimus qui blanditiipraesnt ium volutum deleniti atque crupquos</p>
<div class="abs reviewer" style="left:234px;top:2304px">Nolan Brisk</div>
<svg class="abs" style="left:234px;top:2338px" width="100" height="18" viewBox="0 0 100 18"><g fill="#fff"><path id="s" d="M8 1l2.2 5 5.3.4-4 3.5 1.3 5.2L8 12.3 3.2 15.1l1.3-5.2-4-3.5 5.3-.4z"/><use href="#s" x="21"/><use href="#s" x="42"/><use href="#s" x="63"/></g><use href="#s" x="84" fill="none" stroke="#fff" stroke-width="1.3"/></svg>

<div class="abs avatar" style="left:457px;top:2204px" role="img" aria-label="Client portrait"></div>
<p class="abs quote" style="left:545px;top:2204px"><b>//</b>At vero eos et accusamus et iustodio dignissimos ducimus qui blanditiipraesnt ium volutum deleniti atque crupquos</p>
<div class="abs reviewer" style="left:545px;top:2304px">Nolan Brisk</div>
<svg class="abs" style="left:545px;top:2338px" width="100" height="18" viewBox="0 0 100 18"><g fill="#fff"><use href="#s"/><use href="#s" x="21"/><use href="#s" x="42"/><use href="#s" x="63"/></g><use href="#s" x="84" fill="none" stroke="#fff" stroke-width="1.3"/></svg>

<div class="abs avatar" style="left:770px;top:2204px" role="img" aria-label="Client portrait"></div>
<p class="abs quote" style="left:858px;top:2204px"><b>//</b>At vero eos et accusamus et iustodio dignissimos ducimus qui blanditiipraesnt ium volutum deleniti atque crupquos</p>
<div class="abs reviewer" style="left:858px;top:2304px">Nolan Brisk</div>
<svg class="abs" style="left:858px;top:2338px" width="100" height="18" viewBox="0 0 100 18"><g fill="#fff"><use href="#s"/><use href="#s" x="21"/><use href="#s" x="42"/><use href="#s" x="63"/></g><use href="#s" x="84" fill="none" stroke="#fff" stroke-width="1.3"/></svg>

<section class="abs newsletter"></section>
<h2 class="abs news-title">SIGN UP TO <span>OUR NEWSLETTER</span></h2>
<p class="abs news-text">Sed ut perspiciatis unde omnis iste natus error sit voluptatem accusantium doloremque laudantium, totam rem aperiam, eaque ipsa quae</p>
<div class="abs email">Enter Email</div>
<div class="abs btn-red subscribe">SUBSCRIBE</div>

<svg class="abs" style="left:0;top:2770px" width="1200" height="461" viewBox="0 0 1200 461"><path d="M0 30 C300 0 900 0 1200 30 V461 H0Z" fill="#20222f"/><line x1="0" y1="348" x2="1200" y2="348" stroke="#2c2f3d" stroke-width="1"/></svg>

<div class="abs foot-brand-mark"><span></span></div>
<div class="abs foot-brand-name">Pebble7dock</div>
<div class="abs social" style="left:190px;top:3022px"></div>
<div class="abs social" style="left:232px;top:3022px"></div>

<div class="abs footer-col-title" style="left:392px;top:2864px">ABOUT PEBBLE7DOCK</div>
<p class="abs footer-text" style="left:392px;top:2905px;width:180px">Sed ut perspiciatis unde omnis iste natus error sit voluptatem accusantium doloremque laudantium, totam rem aperiam</p>

<div class="abs footer-col-title" style="left:646px;top:2866px">CONTACT US</div>
<svg class="abs" style="left:650px;top:2922px" width="16" height="20" viewBox="0 0 16 20"><path d="M8 0a7 7 0 0 1 7 7c0 5-7 13-7 13S1 12 1 7a7 7 0 0 1 7-7z" fill="#fff"/><circle cx="8" cy="7" r="2.6" fill="#20222f"/></svg>
<p class="abs footer-text" style="left:683px;top:2916px;line-height:22px;font-size:13.5px">Pebble7dock<br>48 Larkspur Lane<br>Millbrook Falls, NY, 10990</p>
<svg class="abs" style="left:648px;top:2994px" width="18" height="18" viewBox="0 0 18 18"><path d="M4 1l3 4-2 2c1 2.5 3.5 5 6 6l2-2 4 3-2 3C8 17 1 10 1 4z" fill="#fff"/></svg>
<p class="abs footer-text" style="left:682px;top:2990px;line-height:22px;font-size:13.5px">Phone:<br>555-014-2277</p>

<div class="abs footer-col-title" style="left:929px;top:2864px">QUICK LINKS</div>
<p class="abs footer-text" style="left:933px;top:2905px">About Us<br>FAQs<br>Terms of Service<br>Privacy Policy<br>Contact Us</p>

<div class="abs copyright">Pebble7dock © 2019 All Rights Reserved | Privacy Policy | Terms and Conditions</div>

</body>
</html>
```